Meadow Crate Co came about when a life change having to do with my health became an issue and I had to change my diet. We’re a homeschool family and learned a more simplistic way to eat and live out our day to day. We’re ready to share how we eat. Included are attachments to give a visual to the concepts in mind. The first attachment is the logo the second is basically the main idea of the company referencing to getting to the roots of nutrition and juicing. The roots design CONCEPT would be incorporated onto the bottle label. The third attachment is representing the clear stickers we’d like to have on bottles. The 4th and Last are the bottle design we’re looking to use. We’d like tall cylinder bottles.

Label must haves :
meadow crate co logo and the quote know your roots
The roots design
MeadowCrateCo.example

```html
<!DOCTYPE html>
<html lang="en">
<head>
<meta charset="utf-8">
<title>Meadow Crate Co — Label Front &amp; Back</title>
<link rel="stylesheet" href="https://fonts.googleapis.com/css2?family=Arimo:wght@700&family=Fredoka:wght@600&family=Montserrat:wght@500;600;700&display=swap">
<style>
  :root {
    --backdrop: #58585a;
    --card: #ffffff;
    --ink: #6d6e70;
    --ink-soft: #7a7b7d;
    --disc: #c8c9cb;
  }
  * { box-sizing: border-box; margin: 0; padding: 0; }
  html, body { width: 1200px; height: 1154px; overflow: hidden; }
  body { background: var(--backdrop); position: relative; font-family: "Montserrat", Arial, sans-serif; color: var(--ink); }

  .label { position: absolute; top: 110px; width: 460px; height: 935px; background: var(--card); }
  .label--front { left: 114px; }
  .label--back { left: 626px; }

  /* Front */
  .brand { position: absolute; left: 0; top: 60px; width: 460px; height: 260px; }
  .brand__disc { position: absolute; left: 118px; top: 20px; width: 236px; height: 236px; border-radius: 50%; background: var(--disc); }
  .brand__name { position: absolute; left: 0; top: 52px; width: 460px; text-align: center; font-family: "Fredoka", sans-serif; font-weight: 600; font-size: 50px; line-height: 56px; color: var(--ink); }

  .motto { position: absolute; left: 0; top: 378px; width: 460px; text-align: center; font-family: "Fredoka", sans-serif; font-weight: 600; font-size: 64px; line-height: 72px; color: var(--ink); letter-spacing: -1px; }

  .roots-art { position: absolute; left: 38px; top: 530px; width: 384px; height: 132px; background: radial-gradient(ellipse at 50% 20%, #8a8b8d 0%, #a9aaac 45%, #ffffff 75%); }

  .product { position: absolute; left: 46px; top: 706px; width: 380px; height: 110px; }
  .product__ingredients { position: absolute; left: 0; top: 0; width: 210px; font-family: "Arimo", Arial, sans-serif; font-weight: 700; font-size: 13px; line-height: 17px; color: var(--ink); }
  .product__icons { position: absolute; left: 0; top: 66px; display: flex; gap: 7px; }
  .product__icons .badge { width: 34px; height: 34px; }
  .product__divider { position: absolute; left: 212px; top: 0; width: 3px; height: 107px; background: var(--ink); }
  .product__type { position: absolute; left: 228px; top: 0; font-family: "Montserrat", sans-serif; font-weight: 600; font-size: 31px; line-height: 31px; color: var(--ink); }

  .site { position: absolute; left: 0; top: 850px; width: 460px; text-align: center; font-family: "Montserrat", sans-serif; font-weight: 600; font-size: 31px; color: var(--ink); }

  /* Back */
  .copy { position: absolute; left: 56px; width: 362px; }
  .copy__heading { font-weight: 700; font-size: 18px; line-height: 22px; color: var(--ink); margin-bottom: 12px; }
  .copy__body { font-weight: 500; font-size: 14px; line-height: 16.8px; color: var(--ink); }
  .copy--one { top: 129px; }
  .copy--two { top: 333px; }

  .claims { position: absolute; left: 56px; top: 492px; display: flex; gap: 12px; }
  .claims .badge { width: 56px; height: 56px; }
  .claims__list { position: absolute; left: 56px; top: 564px; width: 370px; font-family: "Arimo", Arial, sans-serif; font-weight: 700; font-size: 15.5px; line-height: 20px; color: var(--ink); }

  .tagline { position: absolute; left: 80px; top: 690px; width: 300px; text-align: center; font-family: "Arimo", Arial, sans-serif; font-weight: 700; font-size: 15.5px; line-height: 20px; color: var(--ink); }
</style>
</head>
<body>

  <section class="label label--front">
    <div class="brand">
      <div class="brand__disc"></div>
      <div class="brand__name">Meadow<br>Crate<br>Co</div>
    </div>

    <h1 class="motto">know Your<br>Roots</h1>

    <div class="roots-art" role="img" aria-label="Illustration of spreading plant roots under a soil line"></div>

    <div class="product">
      <p class="product__ingredients">Beetroot, Spirulina, Chlorella, Mushrooms,Pre &amp; Probiotics, Veggies, Vitamins &amp; More!</p>
      <div class="product__icons" aria-label="Dietary badges">
        <svg class="badge" viewBox="0 0 40 40"><circle cx="20" cy="20" r="17" fill="none" stroke="#6d6e70" stroke-width="3"/></svg>
        <svg class="badge" viewBox="0 0 40 40"><circle cx="20" cy="20" r="17" fill="none" stroke="#6d6e70" stroke-width="3"/></svg>
        <svg class="badge" viewBox="0 0 40 40"><circle cx="20" cy="20" r="17" fill="none" stroke="#6d6e70" stroke-width="3"/></svg>
        <svg class="badge" viewBox="0 0 40 40"><circle cx="20" cy="20" r="17" fill="none" stroke="#6d6e70" stroke-width="3"/></svg>
        <svg class="badge" viewBox="0 0 40 40"><circle cx="20" cy="20" r="17" fill="none" stroke="#6d6e70" stroke-width="3"/></svg>
      </div>
      <div class="product__divider"></div>
      <p class="product__type">Cold<br>Preseed<br>Juice</p>
    </div>

    <p class="site">MeadowCrateCo.example</p>
  </section>

  <section class="label label--back">
    <div class="copy copy--one">
      <h2 class="copy__heading">Lorem ipsum</h2>
      <p class="copy__body">Lorem ipsum dolor sit amet, consectetuer adipiscing elit, sed diam nonummy nibh euismod tincidunt ut laoreet dolore magna aliquam erat volutpat. Ut wisi enim ad minim veniam, quis nostrud exerci tation ullamcorper suscipit lobortis nisl ut aliquip ex ea commodo consequat. Duis autem vel eum iriure dolor in hendrerit in vulputate velit esse molestie consequat, vel illum dolore eu feugiat nulla facilisis.</p>
    </div>

    <div class="copy copy--two">
      <h2 class="copy__heading">Lorem ipsum</h2>
      <p class="copy__body">Lorem ipsum dolor sit amet, consectetuer adipiscing elit, sed diam nonummy nibh euismod tincidunt ut laoreet dolore magna aliquam erat volutpat. Ut wisi enim ad minim veniam, quis nostrud exerci tation ullamcorper suscipit lobortis nisl ut aliquip ex ea commodo consequat.</p>
    </div>

    <div class="claims" aria-label="Dietary badges">
      <svg class="badge" viewBox="0 0 40 40"><circle cx="20" cy="20" r="17.5" fill="none" stroke="#6d6e70" stroke-width="2.5"/></svg>
      <svg class="badge" viewBox="0 0 40 40"><circle cx="20" cy="20" r="17.5" fill="none" stroke="#6d6e70" stroke-width="2.5"/></svg>
      <svg class="badge" viewBox="0 0 40 40"><circle cx="20" cy="20" r="17.5" fill="none" stroke="#6d6e70" stroke-width="2.5"/></svg>
      <svg class="badge" viewBox="0 0 40 40"><circle cx="20" cy="20" r="17.5" fill="none" stroke="#6d6e70" stroke-width="2.5"/></svg>
      <svg class="badge" viewBox="0 0 40 40"><circle cx="20" cy="20" r="17.5" fill="none" stroke="#6d6e70" stroke-width="2.5"/></svg>
    </div>
    <p class="claims__list">Beetroot, Spirulina, Chlorella, Mushrooms, Pre &amp; Probiotics,Veggies, Vitamins &amp; More!</p>

    <p class="tagline">Lorem ipsum dolor sit amet, consectetuer adipiscing elit, sed diam nonummy nibh euismod tincidunt ut laoreet dolore</p>

    <p class="site">MeadowCrateCo.example</p>
  </section>

</body>
</html>
```